Business Card and Letterhead for Nurlo - modern real estate business

I need a double sided business card design for Nurlo. Please see business card brief here https://papers.trelvimo.net/sheet/q/7XrTbaLeZpMmQ2uWvd9HkCj4yNoEfsGi3lRtAz_pk/view?mode=shared

Please feel free to design the business cards however you feel best. I am happy to give some creative freedoms and then provide feedback from there.

Please then also create a letterhead to match the business card design

Colors

Designer to choose colors to be used in the design.

Requirements
Must have
• Must be a modern, elegant business card which looks very professional

```html
<!DOCTYPE html>
<html lang="en">
<head>
<meta charset="utf-8">
<title>Nurlo – Business Card and Letterhead</title>
<link rel="stylesheet" href="https://fonts.googleapis.com/css2?family=Montserrat:wght@400;500;700;800&family=Roboto:wght@300;400;500&display=swap">
<style>
  :root {
    --bg: #e4e4e4;
    --card-dark: #1b1b1c;
    --red: #e0202a;
    --red-deep: #9c1118;
    --grey-line: #b9b9bd;
    --white: #ffffff;
    --paper: #fbfbfc;
    --ink: #3a3a3d;
    --faint: #eeeef1;
  }
  * { box-sizing: border-box; margin: 0; padding: 0; }
  html, body { width: 750px; height: 1200px; overflow: hidden; background: var(--bg); }
  body { position: relative; font-family: "Roboto", Arial, sans-serif; }

  .card {
    position: absolute; width: 340px; height: 208px; top: 110px;
    background: var(--card-dark); overflow: hidden;
    box-shadow: 0 6px 18px rgba(0,0,0,.18);
  }
  .card--front { left: 25px; }
  .card--back { left: 385px; }

  .map-area {
    position: absolute; left: 40px; top: 26px; width: 260px; height: 140px;
    background: radial-gradient(ellipse at center, #2c2c2e 0%, #222224 60%, rgba(27,27,28,0) 100%);
  }
  .front-logo {
    position: absolute; left: 0; right: 0; top: 66px; text-align: center;
    font-family: "Montserrat", Arial, sans-serif; font-weight: 800;
    font-size: 50px; letter-spacing: 4px; color: var(--red);
  }
  .front-web {
    position: absolute; left: 0; right: 0; top: 140px; text-align: center;
    font-size: 12px; letter-spacing: 1px; color: var(--white);
  }
  .accent { color: var(--red); }

  .photo-area {
    position: absolute; right: 0; top: 20px; width: 150px; height: 168px;
    background: linear-gradient(160deg, #5a4a44 0%, #3a3c44 45%, #1f2126 100%);
  }
  .agent { position: absolute; left: 20px; top: 36px; }
  .agent-name {
    font-family: "Montserrat", Arial, sans-serif; font-weight: 800;
    font-size: 15px; color: var(--red); letter-spacing: .5px;
  }
  .agent-title { font-size: 11px; color: var(--white); margin-top: 2px; }
  .contact { position: absolute; left: 20px; top: 104px; color: var(--white); font-size: 10px; line-height: 13px; }
  .contact-list { list-style: none; margin-top: 6px; }
  .contact-list li { display: flex; align-items: center; gap: 6px; }
  .contact-list svg { width: 9px; height: 9px; fill: var(--red); }
  .band { position: absolute; left: 0; bottom: 0; width: 100%; height: 100%; pointer-events: none; }
  .card-abn {
    position: absolute; right: 12px; bottom: 7px; font-size: 9px; color: var(--white); letter-spacing: .3px;
  }

  .letterhead {
    position: absolute; left: 125px; top: 420px; width: 500px; height: 707px;
    background: var(--paper); overflow: hidden;
    box-shadow: 0 8px 22px rgba(0,0,0,.16);
    color: var(--ink);
  }
  .lh-logo {
    position: absolute; left: 40px; top: 44px;
    font-family: "Montserrat", Arial, sans-serif; font-weight: 800; font-size: 30px;
    letter-spacing: 2px; color: var(--red);
  }
  .lh-header { position: absolute; right: 34px; top: 44px; display: flex; gap: 14px; font-size: 8px; line-height: 11px; }
  .lh-block { border-left: 1.5px solid var(--red); padding-left: 7px; }
  .lh-block-name { font-family: "Montserrat", Arial, sans-serif; font-weight: 800; color: var(--red); font-size: 8px; }
  .lh-block ul { list-style: none; }
  .lh-block li { display: flex; align-items: center; gap: 4px; }
  .lh-block svg { width: 7px; height: 7px; fill: var(--red); }

  .watermark {
    position: absolute; right: -10px; bottom: 110px;
    font-family: "Montserrat", Arial, sans-serif; font-weight: 800; font-size: 120px;
    letter-spacing: 8px; color: var(--faint);
  }
  .lh-body { position: absolute; left: 60px; top: 140px; width: 380px; font-family: "Montserrat", Arial, sans-serif; font-size: 9.5px; line-height: 13.5px; }
  .recipient-name { text-transform: uppercase; font-weight: 500; }
  .date { margin: 12px 0 10px; }
  .lh-body p.para { margin-bottom: 14px; text-align: left; }
  .regards { margin-top: 26px; }
  .lh-footer-text {
    position: absolute; right: 18px; bottom: 9px; font-size: 8.5px; color: var(--white); letter-spacing: .3px;
  }
</style>
</head>
<body>

  <section class="card card--front" aria-label="Business card front">
    <div class="map-area" role="img" aria-label="Dotted world map in dark grey"></div>
    <div class="front-logo">NURLO</div>
    <div class="front-web">www.<span class="accent">nurlo</span>.com</div>
  </section>

  <section class="card card--back" aria-label="Business card back">
    <div class="photo-area" role="img" aria-label="Portrait photo of the agent in a dark blazer"></div>
    <div class="agent">
      <div class="agent-name">DANE MAXWELL</div>
      <div class="agent-title">Licenced Real Estate Agent</div>
    </div>
    <div class="contact">
      <div>PO Box 6130<br>Brackenvale NSW 2790</div>
      <ul class="contact-list">
        <li><svg viewBox="0 0 10 10"><path d="M2 0.5 L4 2.5 L3 3.8 Q4.5 6 6.2 7 L7.5 6 L9.5 8 L8 9.5 Q3 9 0.5 2 Z"/></svg>0412 308 519</li>
        <li><svg viewBox="0 0 10 10"><path d="M0 2 H10 V8 H0 Z M0 2 L5 5.5 L10 2" /></svg>dane@nurlo.com</li>
        <li><svg viewBox="0 0 10 10"><circle cx="5" cy="5" r="4.6"/></svg>www.<span class="accent">nurlo</span>.com</li>
      </ul>
    </div>
    <svg class="band" viewBox="0 0 340 208" preserveAspectRatio="none" aria-hidden="true">
      <defs>
        <linearGradient id="cardRed" x1="0" x2="1">
          <stop offset="0" stop-color="#9c1118"/><stop offset=".6" stop-color="#e0202a"/><stop offset="1" stop-color="#c4161f"/>
        </linearGradient>
      </defs>
      <polygon points="0,193 192,193 210,176 212,176 194,195 0,195" fill="#b9b9bd"/>
      <polygon points="0,198 200,198 218,182 340,182 340,208 0,208" fill="url(#cardRed)"/>
    </svg>
    <div class="card-abn">ABN: 41 208 965 330</div>
  </section>

  <section class="letterhead" aria-label="Letterhead">
    <div class="watermark" aria-hidden="true">NURLO</div>
    <div class="lh-logo">NURLO</div>
    <div class="lh-header">
      <div class="lh-block">
        <div class="lh-block-name">NURLO</div>
        <div>PO Box 6130</div>
        <div>Brackenvale NSW 2790</div>
      </div>
      <div class="lh-block">
        <ul>
          <li><svg viewBox="0 0 10 10"><path d="M2 0.5 L4 2.5 L3 3.8 Q4.5 6 6.2 7 L7.5 6 L9.5 8 L8 9.5 Q3 9 0.5 2 Z"/></svg>0412 308 519</li>
          <li><svg viewBox="0 0 10 10"><path d="M0 2 H10 V8 H0 Z"/></svg>dane@nurlo.com</li>
          <li><svg viewBox="0 0 10 10"><circle cx="5" cy="5" r="4.6"/></svg>www.<span class="accent">nurlo</span>.com</li>
        </ul>
      </div>
    </div>

    <div class="lh-body">
      <div class="recipient-name">Oliver Grant</div>
      <div>Managing Director</div>
      <div class="date">Date : 01 October 2019</div>
      <p class="para">Lorem ipsum dolor sit amet, consectetur adipisicing elit, sed do eiusmod tempor incididunt ut labore et dolore magna aliqua. Ut enim ad minim veniam, quis nostrud exercitation ullamco laboris nisi ut aliquip ex ea commodo consequat. Duis aute irure dolor in reprehenderit in voluptate velit esse cillum dolore eu fugiat nulla pariatur. Excepteur sint occaecat cupidatat non proident, sunt in culpa qui officia deserunt mollit anim id est laborum. re et dolore magnam aliquam quaerat voluptatem.</p>
      <p class="para">Lorem ipsum dolor sit amet, consectetur adipisicing elit, sed do eiusmod tempor incididunt ut labore et dolore magna aliqua. Ut enim ad minim veniam, quis nostrud exercitation ullamco laboris nisi ut aliquip ex ea commodo consequat. Duis aute irure dolor in reprehenderit in voluptate velit esse cillum dolore eu fugiat nulla pariatur. Excepteur sint occaecat cupidatat non proident, sunt in culpa qui officia deserunt mollit anim id est laborum. re et dolore magnam aliquam quaerat voluptatem.</p>
      <div class="regards">Regards</div>
    </div>

    <svg class="band" viewBox="0 0 500 707" preserveAspectRatio="none" aria-hidden="true">
      <defs>
        <linearGradient id="lhRed" x1="0" x2="1">
          <stop offset="0" stop-color="#9c1118"/><stop offset=".6" stop-color="#e0202a"/><stop offset="1" stop-color="#b8141d"/>
        </linearGradient>
      </defs>
      <polygon points="0,688 300,688 322,666 326,666 304,691 0,691" fill="#b9b9bd"/>
      <polygon points="0,696 310,696 332,672 500,672 500,707 0,707" fill="url(#lhRed)"/>
    </svg>
    <div class="lh-footer-text">ABN: 41 208 965 330 &nbsp;|&nbsp; Lic No. 204817</div>
  </section>

</body>
</html>
```